Quorvane Consulting

We focus on Data Recovery but we also do Network Security. We recover data from all types of hard drive form factors 3.5", 2.5", 1", 1.8", 5.25", 8" with any kind of interface IDE(PATA), SATA, mSATA, SCSI, SAS and Fibre Channel. All RAID Arrays 0, 1, 2, 3, 4, 5, 10 including nested levels like RAID 0+1, 1+0, 100, 0+3, 50 and 60, flash drives, like tablets, cellphones, usb drives, memory cards(SD, miniSD, Memory Stick(hovaku))

Actually you can gather any information or text from any data recovery site, cause is usually the same info, we would probably change a couple of things from the description so it wont look the same. One thing though, we want to make clear to users not to attempt data recovery themselves and to ship the faulty device to us, maybe we can illustrate this?

the Data Recovery link can have sub menus like "Data Recovery Process - Data Recovery Services - F.A.Q"

the Penetration Testing can have sub menus like "F.A.Q - Pentest Process - Pentest Services"

Here are links from website so you gather information:

-http://www.brelwick-disks.example/

-http://www.tolvenpathrescue.example/

-http://www.nimbrocore.example/

http://fentaloprestore.example/lp/disk-restore.aspx?src=web&ref=ZQPLx4TrmvaKDJ-wuHafk9RB2x
http://www.vqlt.example/
http://www.pembrastoneflow.example/data-recovery/
http://www.ytsarchiverescue.example/

thanks.

Target Market(s)

Any PC user

Industry/Entity Type

Data Recovery

Requirements
Must have
• - Language and geographic navigation
- Home page navigation
- Global navigation
- Breadcrumbs
Nice to have
• - Sliders
-Drop down navigation

```html
<!DOCTYPE html>
<html lang="en">
<head>
<meta charset="utf-8">
<title>Quorvane Consulting – Expert Data Recovery</title>
<link href="https://fonts.googleapis.com/css2?family=Ubuntu:wght@300;400;500;700&family=Arimo:wght@400;700&display=swap" rel="stylesheet">
<style>
:root{
  --red:#e41e26;
  --red-dark:#c3141b;
  --ink:#2b2b2b;
  --hero:#242424;
  --paper:#ebebeb;
  --footer:#303030;
  --footer-deep:#222222;
  --muted:#555;
  --white:#fff;
  --line:#d6d6d6;
}
*{margin:0;padding:0;box-sizing:border-box}
html,body{width:960px;height:1200px;overflow:hidden}
body{position:relative;background:var(--paper);font-family:"Arimo",Arial,sans-serif;color:var(--ink)}
.abs{position:absolute}

/* header */
.site-header{left:0;top:0;width:960px;height:108px;background:linear-gradient(#fff,#f3f3f3)}
.header-rule{left:0;top:108px;width:960px;height:10px;background:#dcdcdc}
.brand{left:90px;top:40px;display:flex;align-items:center;gap:8px;font-family:"Ubuntu",sans-serif;font-weight:700;font-size:22px;color:var(--ink)}
.brand-mark{width:18px;height:18px;background:var(--red)}
.call-note{right:89px;top:10px;font-size:9.5px;font-family:"Ubuntu",sans-serif}
.call-note b{color:var(--red);font-weight:400}
.call-phone{right:89px;top:25px;font-family:"Ubuntu",sans-serif;font-weight:500;font-size:18px;display:flex;align-items:center;gap:5px}
.main-nav{left:366px;top:58px;width:509px;height:30px;background:var(--red);border-radius:3px;display:flex;align-items:center;padding:0 3px;font-family:"Ubuntu",sans-serif;font-size:10px;color:var(--white)}
.main-nav span{padding:0 12px;line-height:24px;white-space:nowrap}
.main-nav .active{background:#111;border-radius:3px}

/* hero */
.hero{left:0;top:118px;width:960px;height:338px;background:radial-gradient(ellipse at 30% 40%,#333,var(--hero) 70%)}
.hero-title{left:100px;top:160px;color:var(--white);font-family:"Arimo",sans-serif;font-size:44px;letter-spacing:.5px}
.hero-word{left:96px;top:200px;color:var(--red);font-family:"Arimo",sans-serif;font-size:78px;letter-spacing:-1px}
.hero-copy{left:100px;top:286px;width:340px;color:var(--white);font-family:"Ubuntu",sans-serif;font-weight:300;font-size:14px;line-height:19.5px}
.hero-btn{left:99px;top:348px;width:212px;height:37px;background:var(--red);border-radius:3px;color:var(--white);font-family:"Ubuntu",sans-serif;font-size:21px;display:flex;align-items:center;padding-left:10px;gap:8px}
.hero-art{left:495px;top:132px;width:360px;height:318px;border-radius:8px;background:radial-gradient(circle at 45% 45%,#e8e8e8 0 30%,#7a7a7a 45%,#3a3a3a 70%,transparent 72%)}

/* content cards */
.card{background:var(--white);border:1px solid var(--line);border-radius:5px;box-shadow:0 1px 3px rgba(0,0,0,.12)}
.help{left:100px;top:498px;width:226px;height:132px}
.help h2{position:absolute;left:11px;top:13px;font-family:"Ubuntu",sans-serif;font-size:20px;font-weight:500;white-space:nowrap}
.help .num{position:absolute;left:11px;top:42px;font-family:"Ubuntu",sans-serif;font-size:19px;color:var(--red);white-space:nowrap;z-index:2}
.help .btn{position:absolute;left:11px;top:86px;width:110px;height:24px;background:var(--red);border-radius:4px;color:var(--white);font-family:"Ubuntu",sans-serif;font-size:10px;line-height:24px;padding-left:7px;white-space:nowrap;z-index:2}
.help-art{position:absolute;left:140px;top:52px;width:80px;height:70px;border-radius:10px;background:linear-gradient(135deg,#bcd6ec,#6c8fb1);z-index:1}

.intro-title{left:344px;top:500px;font-family:"Ubuntu",sans-serif;font-size:24.5px;font-weight:400;color:var(--red);white-space:nowrap}
.intro-copy{left:347px;top:535px;width:513px;font-size:10px;line-height:14.4px;color:var(--muted)}

.panel-head{position:absolute;left:5px;top:5px;width:219px;height:32px;background:var(--red);border-radius:3px;color:var(--white);font-family:"Ubuntu",sans-serif;font-weight:300;font-size:16.5px;line-height:32px;padding-left:8px;white-space:nowrap}
.resources{left:100px;top:662px;width:230px;height:246px}
.resources ul{position:absolute;left:7px;top:52px;width:214px;list-style:none}
.resources li{height:22.4px;border-bottom:1px dotted #ccc;font-size:10px;line-height:22px;display:flex;align-items:center;gap:6px;white-space:nowrap;overflow:hidden}
.resources li:last-child{border-bottom:none}
.blog{left:356px;top:662px;width:230px;height:246px}
.post{position:absolute;left:11px;width:210px;height:40px}
.post .avatar{position:absolute;left:0;top:2px;width:38px;height:36px;background:linear-gradient(#b9b2a8,#6f6a64)}
.post .date{position:absolute;right:0;top:0;font-size:9px;color:var(--red)}
.post p{position:absolute;left:47px;top:13px;font-size:10px;line-height:13px}

.spec-1{left:608px;top:669px;font-family:"Ubuntu",sans-serif;font-weight:400;font-size:19.5px;color:var(--red);white-space:nowrap}
.spec-2{left:608px;top:694px;font-family:"Ubuntu",sans-serif;font-size:25px;color:var(--ink);font-weight:500;white-space:nowrap}
.video{left:609px;top:733px;width:254px;height:174px;padding:2px}
.video-art{width:100%;height:100%;background:linear-gradient(120deg,#3d3d3d,#c9c9c9 55%,#7e7e7e);position:relative}
.video-art svg{position:absolute;left:99px;top:46px}

/* partners & footer */
.site-footer{left:0;top:1006px;width:960px;height:167px;background:var(--footer)}
.partners{left:101px;top:976px;width:773px;height:73px;background:var(--white);border-radius:5px;box-shadow:0 1px 3px rgba(0,0,0,.2)}
.partner{position:absolute;top:16px;background:#c9c9c9;border-radius:3px}
.arrow-ctl{position:absolute;top:22px;font-size:28px;color:#333;font-family:"Ubuntu",sans-serif}
.foot-list{list-style:none;color:var(--white);font-family:"Ubuntu",sans-serif;font-size:11px}
.foot-list li{height:20.8px;display:flex;align-items:center;gap:8px;white-space:nowrap}
.social li{gap:7px}
.social i{display:inline-block;width:15px;height:15px;border-radius:3px}
.news-title{left:629px;top:1065px;color:var(--white);font-family:"Ubuntu",sans-serif;font-weight:500;font-size:15px}
.news-copy{left:629px;top:1093px;width:250px;color:var(--white);font-size:10px;line-height:14.4px}
.news-field{left:630px;top:1131px;width:201px;height:29px;background:#5b5b5b;border-radius:3px 0 0 3px}
.news-btn{left:831px;top:1131px;width:37px;height:29px;background:var(--red);border-radius:0 3px 3px 0;display:flex;align-items:center;justify-content:center}
.copyright{left:0;top:1173px;width:960px;height:27px;background:var(--footer-deep);color:var(--white);font-size:10px;text-align:center;line-height:27px}
</style>
</head>
<body>

<header class="abs site-header">
  <div class="abs brand"><span class="brand-mark"></span>Quorvane Consulting</div>
  <div class="abs call-note">Call today for a <b>FREE</b> estimate!</div>
  <div class="abs call-phone">
    <svg width="17" height="17" viewBox="0 0 20 20"><circle cx="10" cy="10" r="10" fill="#e41e26"/><path d="M5 8c0-2 10-2 10 0v1h-3V8H8v1H5zM6 10h8l1 5H5z" fill="#fff"/></svg>
    (555) 204-7719
  </div>
  <nav class="abs main-nav">
    <span class="active">HOME</span><span>ABOUT US</span><span>HARD DRIVE RECOVERY</span><span>DATA RECOVERY TRANING</span><span>SERVICES</span>
  </nav>
</header>
<div class="abs header-rule"></div>

<section class="abs hero"></section>
<div class="abs hero-title">EXPERT DATA</div>
<div class="abs hero-word">Recovery</div>
<p class="abs hero-copy">Pembrastone provides state-of-the-art data recovery services, data recovery software.</p>
<div class="abs hero-btn">More Infomation
  <svg width="22" height="18" viewBox="0 0 22 18"><path d="M2 2l7 7-7 7M11 2l7 7-7 7" stroke="#fff" stroke-width="2.4" fill="none"/></svg>
</div>
<div class="abs hero-art" role="img" aria-label="Open laptop hard drive showing platter and read arm"></div>

<div class="abs card help">
  <h2>Need Help Now?</h2>
  <div class="num">555 318 0264</div>
  <div class="btn">Request an Estimate &nbsp;›</div>
  <div class="help-art" role="img" aria-label="Desk telephone illustration"></div>
</div>

<h1 class="abs intro-title">Your 24/7 Data Recovery Heroes</h1>
<p class="abs intro-copy">simply dummy text of the printing and typesetting industry. Lorem Ipsum has been the industry's standard dummy text ever since the 1500s, when an unknown printer took a galley of type and scrambled it to make a type specimen book. It has survived not only five centuries, but also the leap into electronic typesetting, remaining essentially &nbsp;when an unknown printer took a galley of type and scrambled it to make a type specimen book. It has survived not only five centuries, but also the leap into electronic typesetting, remaining essentially unchanged. It was popularised in the 1960s with the release of Lettrafix sheets containing</p>

<section class="abs card resources">
  <div class="panel-head">Presentations &amp; Resources</div>
  <ul>
    <li><svg width="12" height="8" viewBox="0 0 12 8"><path d="M1 4h9M7 1l3 3-3 3" stroke="#e41e26" fill="none"/></svg>Altrona vs Deepmoor Imager</li>
    <li><svg width="12" height="8" viewBox="0 0 12 8"><path d="M1 4h9M7 1l3 3-3 3" stroke="#e41e26" fill="none"/></svg>HDQM Podcast #16 is Published</li>
    <li><svg width="12" height="8" viewBox="0 0 12 8"><path d="M1 4h9M7 1l3 3-3 3" stroke="#e41e26" fill="none"/></svg>Representation Techfair in Sydney Australia</li>
    <li><svg width="12" height="8" viewBox="0 0 12 8"><path d="M1 4h9M7 1l3 3-3 3" stroke="#e41e26" fill="none"/></svg>BKTP Podcast on Solid Stated Drives and</li>
    <li><svg width="12" height="8" viewBox="0 0 12 8"><path d="M1 4h9M7 1l3 3-3 3" stroke="#e41e26" fill="none"/></svg>New Technology</li>
    <li><svg width="12" height="8" viewBox="0 0 12 8"><path d="M1 4h9M7 1l3 3-3 3" stroke="#e41e26" fill="none"/></svg>BKTP Two Hour Podcast on Everything you</li>
    <li><svg width="12" height="8" viewBox="0 0 12 8"><path d="M1 4h9M7 1l3 3-3 3" stroke="#e41e26" fill="none"/></svg>wanted to know about Hard Drives!</li>
    <li><svg width="12" height="8" viewBox="0 0 12 8"><path d="M1 4h9M7 1l3 3-3 3" stroke="#e41e26" fill="none"/></svg>Cell Phone Providers Retention Periods</li>
  </ul>
</section>

<section class="abs card blog">
  <div class="panel-head">Latest Blog Posts</div>
  <div class="post" style="top:56px"><div class="avatar" role="img" aria-label="Author portrait"></div><span class="date">December 31. 2012</span><p>The industry's standard dummy text ever since the 1500s.</p></div>
  <div class="post" style="top:101px"><div class="avatar" role="img" aria-label="Author portrait"></div><span class="date">December 31. 2012</span><p>The industry's standard dummy text ever since the 1500s.</p></div>
  <div class="post" style="top:146px"><div class="avatar" role="img" aria-label="Author portrait"></div><span class="date">December 31. 2012</span><p>The industry's standard dummy text ever since the 1500s.</p></div>
  <div class="post" style="top:194px"><div class="avatar" role="img" aria-label="Author portrait"></div><span class="date">December 31. 2012</span><p>The industry's standard dummy text ever since the 1500s.</p></div>
</section>

<h2 class="abs spec-1">Hard Drive Data Recovery is</h2>
<h2 class="abs spec-2">Our specialty...</h2>
<div class="abs card video">
  <div class="video-art" role="img" aria-label="Technician in clean-room suit working on an open hard drive">
    <svg width="54" height="54" viewBox="0 0 54 54"><circle cx="27" cy="27" r="27" fill="#333" opacity=".85"/><path d="M21 15l18 12-18 12z" fill="#fff"/></svg>
  </div>
</div>

<footer class="abs site-footer"></footer>
<div class="abs partners">
  <span class="arrow-ctl" style="left:10px">‹</span>
  <div class="partner" style="left:36px;width:43px;height:43px;background:#222"></div>
  <div class="partner" style="left:106px;width:73px;height:28px;top:22px"></div>
  <div class="partner" style="left:206px;width:32px;height:52px;top:10px"></div>
  <div class="partner" style="left:268px;width:74px;height:44px;top:12px"></div>
  <div class="partner" style="left:357px;width:70px;height:34px;border-radius:17px"></div>
  <div class="partner" style="left:452px;width:78px;height:34px;border-radius:17px"></div>
  <div class="partner" style="left:551px;width:76px;height:42px;top:14px"></div>
  <div class="partner" style="left:652px;width:80px;height:24px;top:24px"></div>
  <span class="arrow-ctl" style="left:754px">›</span>
</div>

<ul class="abs foot-list" style="left:110px;top:1068px">
  <li><svg width="14" height="8" viewBox="0 0 14 8"><path d="M0 4h12M9 1l3 3-3 3" stroke="#e41e26" stroke-width="1.6" fill="none"/></svg>Home</li>
  <li><svg width="14" height="8" viewBox="0 0 14 8"><path d="M0 4h12M9 1l3 3-3 3" stroke="#e41e26" stroke-width="1.6" fill="none"/></svg>About Us</li>
  <li><svg width="14" height="8" viewBox="0 0 14 8"><path d="M0 4h12M9 1l3 3-3 3" stroke="#e41e26" stroke-width="1.6" fill="none"/></svg>Hard Drive Recovery</li>
  <li><svg width="14" height="8" viewBox="0 0 14 8"><path d="M0 4h12M9 1l3 3-3 3" stroke="#e41e26" stroke-width="1.6" fill="none"/></svg>Partners</li>
</ul>
<ul class="abs foot-list" style="left:259px;top:1069px">
  <li><svg width="14" height="8" viewBox="0 0 14 8"><path d="M0 4h12M9 1l3 3-3 3" stroke="#e41e26" stroke-width="1.6" fill="none"/></svg>Data Recovery</li>
  <li><svg width="14" height="8" viewBox="0 0 14 8"><path d="M0 4h12M9 1l3 3-3 3" stroke="#e41e26" stroke-width="1.6" fill="none"/></svg>Traning</li>
  <li><svg width="14" height="8" viewBox="0 0 14 8"><path d="M0 4h12M9 1l3 3-3 3" stroke="#e41e26" stroke-width="1.6" fill="none"/></svg>Services</li>
  <li><svg width="14" height="8" viewBox="0 0 14 8"><path d="M0 4h12M9 1l3 3-3 3" stroke="#e41e26" stroke-width="1.6" fill="none"/></svg>Contact Us</li>
</ul>
<ul class="abs foot-list social" style="left:442px;top:1067px;font-size:10.5px">
  <li><i style="background:#3b5998"></i>Follow us Loopwall</li>
  <li><i style="background:#3fa9d8"></i>Follow us Chirrup</li>
  <li><i style="background:#2b7bb9"></i>Follow us Linkvane</li>
  <li><i style="background:#d22b2b"></i>Vidstream</li>
</ul>

<h3 class="abs news-title">Join Our Newsletter</h3>
<p class="abs news-copy">Stay up to date with all our latest tips to improve your websites performance with our newsletter.</p>
<div class="abs news-field"></div>
<div class="abs news-btn">
  <svg width="22" height="18" viewBox="0 0 22 18"><circle cx="8" cy="8" r="6.5" stroke="#fff" stroke-width="1.5" fill="none"/><path d="M1.5 8h13M8 1.5v13M3.5 4h9M3.5 12h9" stroke="#fff" stroke-width=".8"/><path d="M13 12l7 5" stroke="#fff" stroke-width="2.4"/></svg>
</div>

<div class="abs copyright">Copyright © 2013 Quorvane Consulting. All rights reserved.</div>

</body>
</html>
```